Letterhead for financial advisor-insurance agent firm

Our company, Marlowe Thistle Insurance & Investments, is an insurance (health, life, home, auto, etc) and investment brokerage offering a suite of options to meet client needs. We need letterhead that is professional and embodies strength, security and sophistication.

Industry/Entity Type

Investment

```html
<!DOCTYPE html>
<html lang="en">
<head>
<meta charset="utf-8">
<title>Marlowe Thistle Insurance &amp; Investments — Letterhead</title>
<link href="https://fonts.googleapis.com/css2?family=Cormorant+Garamond:wght@500;600&display=swap" rel="stylesheet">
<style>
  :root {
    --paper: #ffffff;
    --navy: #232838;
    --ink: #2a2f40;
    --faint: #e6e7ea;
    --footer-text: #d9dbe2;
  }
  html, body {
    margin: 0;
    padding: 0;
    width: 870px;
    height: 1200px;
    overflow: hidden;
    background: var(--paper);
  }
  .letterhead {
    position: relative;
    width: 870px;
    height: 1200px;
    background: var(--paper);
    font-family: "Cormorant Garamond", Georgia, serif;
    color: var(--ink);
  }
  .brand {
    position: absolute;
    top: 66px;
    right: 28px;
    width: 200px;
    text-align: center;
  }
  .brand-mark {
    display: block;
    width: 44px;
    height: 44px;
    margin: 0 auto 10px;
    border: 2px solid var(--ink);
    box-sizing: border-box;
  }
  .brand-name {
    margin: 0;
    font-size: 19px;
    font-weight: 600;
    letter-spacing: 1.5px;
    text-transform: uppercase;
    line-height: 1.1;
    white-space: nowrap;
  }
  .brand-tagline {
    margin: 3px 0 0;
    font-size: 10px;
    font-weight: 600;
    letter-spacing: 1.5px;
    text-transform: uppercase;
    white-space: nowrap;
  }
  .emblem {
    position: absolute;
    left: 275px;
    top: 350px;
    width: 320px;
    height: 320px;
    overflow: visible;
  }
  .emblem-text {
    font-family: "Cormorant Garamond", Georgia, serif;
    font-size: 42px;
    font-weight: 600;
    letter-spacing: 3px;
    fill: var(--faint);
  }
  .footer-band {
    position: absolute;
    left: 0;
    top: 1090px;
    width: 870px;
    height: 84px;
    background: var(--navy);
  }
  .footer-mark {
    position: absolute;
    left: 598px;
    top: 18px;
    width: 30px;
    height: 30px;
    border: 1.5px solid var(--footer-text);
    box-sizing: border-box;
  }
  .footer-details {
    position: absolute;
    left: 640px;
    top: 16px;
    color: var(--footer-text);
    font-size: 10px;
    line-height: 1.3;
    white-space: nowrap;
  }
  .footer-details p { margin: 0; }
  .footer-name { font-weight: 600; }
  .footer-address { margin-top: 6px !important; }
</style>
</head>
<body>
  <main class="letterhead">
    <header class="brand">
      <span class="brand-mark"></span>
      <p class="brand-name">Marlowe Thistle</p>
      <p class="brand-tagline">Insurance &amp; Investments</p>
    </header>

    <svg class="emblem" viewBox="0 0 320 320" aria-hidden="true">
      <rect x="4" y="4" width="312" height="312" fill="none" stroke="var(--faint)" stroke-width="8"/>
      <rect x="22" y="22" width="276" height="276" fill="none" stroke="var(--faint)" stroke-width="2"/>
      <text class="emblem-text" x="160" y="152" text-anchor="middle">MARLOWE</text>
      <text class="emblem-text" x="160" y="200" text-anchor="middle">THISTLE</text>
    </svg>

    <footer class="footer-band">
      <span class="footer-mark"></span>
      <div class="footer-details">
        <p class="footer-name">Marlowe Thistle</p>
        <p class="footer-name">Insurance &amp; Investments</p>
        <p class="footer-address">48 Harbour Row, Suite 210</p>
        <p>Ashford Park, Cedar Bay, NC 28401</p>
      </div>
    </footer>
  </main>
</body>
</html>
```